Diverse business needs a corporate identity system

Brantow Fielding Holdings Limited is a well established family owned and run business operating in Port Moresby, Papua New Guinea since 1989. As part of taking the business to the next level, we are redoing our branding/corporate identity.

We currently carry out two core business activities servicing corporate clients in the commercial and industrial sectors:
1. Electrical - new installations and maintenance work
2. Construction - mostly commercial & industrial, some residential

We are looking to add the following business activities in near future:
1. IT consulting
2. Property development - business/industrial park, residential complexes, low cost housing
3. Retail of hardware, construction supplies and flat pack furniture & kitchens

We have just completed our logo design here on SketchHarbor and now wanting to design business card and stationery based on our new logo (attached).

Deliverables are:
1. Business card - double sided
2. Letterhead A4

Details to go on the card:
Name: Marcus Trevane
Title: Director
Email: marcus.trevane@brantowfield.com
Tel: +675 3147720, +675 3148815
Office: Section 17 Lot 48, Waravu Light Industrial Area, Port Moresby, Papua New Guinea
Postal: PO Box 419, Waravu, NCD, Papua New Guinea
Website: brantowfield.com

Our services can be listed somewhere on the card:
Electrical, Construction, Property Development, IT Consulting

Details to go on the letterhead:
Brantow Fielding Holdings Ltd.
PO Box 419, Waravu, NCD, Papua New Guinea
Fax: +675 3146603
Email: info@brantowfield.com

For inspiration, I have uploaded some images of business cards we like.

Would be good if the same/similar business card design could be printed both economically (e.g. full coloured both sides, matte card stock) for majority of staff and upscaled to use premium features such as letter pressed, foil etc for use by executives. Otherwise, please provide two separate designs.

Logo text font is nexa bold freefont - please use something from nexa family or another font type that complements it.

Reason: Few designs were submitted. Most were clearly from ready to use templates. No designs really stand out for us at the moment. So we have decided to narrow the focus to just business card and A4 letterhead. And also revised the brief to be completely open to hopefully invite more creative designs.

I have updated the brief to be a lot less restrictive to try and get more creative designs. Also uploaded more images of premium business cards for inspiration.

Industry/Entity Type

Construction

Requirements
Must have
• All designs must conform to printolane specifications. Refer to and download appropriate work file templates from http://www.printolane.com.au/pl/ns/files/UploadResources.aspx?GP=1%2F9%2F2014+12%3A53%3A21+AM&GPS=5829104463&GNF=1&selectedTab=0.
Should not have
• No QR codes and social media links.

```html
<!DOCTYPE html>
<html lang="en">
<head>
<meta charset="utf-8">
<title>Brantow Fielding – Business Card</title>
<link href="https://fonts.googleapis.com/css2?family=Didact+Gothic&family=Questrial&display=swap" rel="stylesheet">
<style>
  :root{
    --bg:#3a3a3a;
    --red:#d33a2c;
    --red-deep:#b72a22;
    --yellow:#f7b823;
    --white:#ffffff;
    --logo-grey:#e6e6e6;
    --text-grey:#8a8a8a;
  }
  *{margin:0;padding:0;box-sizing:border-box}
  html,body{width:1200px;height:1000px;overflow:hidden;background:var(--bg)}
  body{position:relative;font-family:"Didact Gothic","Questrial",sans-serif}
  .card{position:absolute;left:250px;width:700px;height:400px;overflow:hidden;box-shadow:0 6px 18px rgba(0,0,0,.45)}
  .card-back{top:70px;background:linear-gradient(135deg,var(--red) 0%,var(--red-deep) 100%)}
  .card-front{top:530px;background:var(--white)}

  /* back */
  .back-brand{position:absolute;left:150px;top:150px;display:flex;align-items:center;gap:22px}
  .brand-dot{width:70px;height:70px;border-radius:50%;background:var(--logo-grey)}
  .back-brand .brand-name{font-size:58px;color:var(--logo-grey);letter-spacing:-.5px}
  .services{position:absolute;right:34px;bottom:30px;font-size:17px;color:var(--yellow);letter-spacing:.2px}
  .services .sep{opacity:.7;margin:0 6px}

  /* front */
  .accent-strip{position:absolute;left:0;top:0;width:24px;height:100%;background:var(--red)}
  .accent-strip::before{content:"";position:absolute;left:0;top:0;width:100%;height:78px;background:var(--yellow)}
  .front-brand{position:absolute;right:40px;top:36px;display:flex;align-items:center;gap:12px}
  .front-brand .brand-dot{width:46px;height:46px;background:var(--red)}
  .front-brand .brand-name{font-size:26px;color:var(--red)}
  .person{position:absolute;left:60px;top:64px}
  .person-name{font-size:28px;font-weight:700;color:var(--red);font-family:"Questrial",sans-serif;letter-spacing:.3px}
  .person-title{font-size:19px;color:var(--text-grey);margin-top:2px}
  .address{position:absolute;right:40px;top:150px;text-align:right;font-size:19px;line-height:1.3;color:var(--text-grey)}
  .contacts{position:absolute;left:60px;bottom:40px;list-style:none;font-size:19px;color:var(--text-grey);line-height:1.35}
  .contacts li{display:flex;align-items:center;gap:12px}
  .contacts svg{width:18px;height:15px;flex:none}
</style>
</head>
<body>
  <section class="card card-back" aria-label="Business card back">
    <div class="back-brand">
      <span class="brand-dot"></span>
      <span class="brand-name">Brantow Fielding</span>
    </div>
    <p class="services">Electrical<span class="sep">|</span>Construction<span class="sep">|</span>Property Development<span class="sep">|</span>IT Consulting</p>
  </section>

  <section class="card card-front" aria-label="Business card front">
    <div class="accent-strip"></div>
    <div class="front-brand">
      <span class="brand-dot"></span>
      <span class="brand-name">Brantow Fielding</span>
    </div>
    <div class="person">
      <p class="person-name">Adrian Kell Moraga</p>
      <p class="person-title">President</p>
    </div>
    <address class="address" style="font-style:normal">
      Section 17 Lot 48 Waravu,<br>
      Port Moresby, NCD<br>
      Papua New Guinea<br>
      www.brantowfield.com
    </address>
    <ul class="contacts">
      <li><svg viewBox="0 0 18 15"><rect width="18" height="15" rx="3" fill="#f7b823"/><path d="M4 4h10v7H4z M4 4l5 4 5-4" fill="none" stroke="#fff" stroke-width="1.3"/></svg>adrian.moraga@brantowfield.com</li>
      <li><svg viewBox="0 0 18 15"><rect width="18" height="15" rx="3" fill="#f7b823"/><rect x="6" y="3" width="6" height="9" rx="1" fill="none" stroke="#fff" stroke-width="1.3"/></svg>+61.702418396</li>
      <li><svg viewBox="0 0 18 15"><rect width="18" height="15" rx="3" fill="#f7b823"/><path d="M4 7q5-4 10 0v2h-3V7.5H7V9H4z" fill="#fff"/><rect x="5" y="9.5" width="8" height="2.5" fill="#fff"/></svg>+61.731590264</li>
      <li><svg viewBox="0 0 18 15"><rect width="18" height="15" rx="3" fill="#f7b823"/><rect x="4" y="6" width="10" height="6" fill="none" stroke="#fff" stroke-width="1.3"/><rect x="6" y="3" width="6" height="3" fill="#fff"/></svg>+61.748263015</li>
    </ul>
  </section>
</body>
</html>
```